Educational Management System User Interface (Veltrix Design Concepts)

Hi,I require a 1-page design for an educational management system. The image attached shows all required elements and also their locations. I require the design to be based on veltrix-styled interfaces using elements from: http://pramel.examplehost.io/pramel-framekit/ & http://kitnulloa.com/kitnulloa-layout/admin . Side menu's should not be too large that they hide the main content of the page.
Sorry very slight addition to the design as per new uploaded file.
I like how the elements of the veltrix orbit page are seperated with the background colour and white boxes. This could maybe work in the design as per the uploaded image?
Thanks,
Tobias
Reason: Some designers have some submissions.

```html
<!DOCTYPE html>
<html lang="en">
<head>
<meta charset="utf-8">
<title>Lernwell – Dashboard</title>
<link href="https://fonts.googleapis.com/css2?family=Roboto:wght@300;400;500;700&display=swap" rel="stylesheet">
<style>
:root{
  --green:#62b346;
  --green-soft:#8cc474;
  --green-line:#d6ecce;
  --dark:#222222;
  --header-top:#4a4a4a;
  --header-bottom:#1c1c1c;
  --panel:#ececec;
  --white:#ffffff;
  --card:#fafafa;
  --border:#cfcfcf;
  --text:#222222;
  --muted:#555555;
  --avatar:#c89a7c;
  --pdf:#d9262c;
}
*{box-sizing:border-box;margin:0;padding:0}
html,body{width:1200px;height:1015px;overflow:hidden}
body{font-family:'Roboto',sans-serif;color:var(--text);background:var(--white);position:relative}
.abs{position:absolute}
/* header */
.topbar{position:absolute;left:0;top:0;width:1200px;height:101px;background:linear-gradient(var(--header-top),var(--header-bottom))}
.brand{position:absolute;left:58px;top:36px;color:var(--white);font-size:28px;font-weight:500;line-height:34px}
.topnav svg{position:absolute;top:41px}
.user-name{position:absolute;left:934px;top:40px;color:var(--white);font-size:15px;font-weight:500;letter-spacing:.2px}
.avatar{border-radius:50%;background:radial-gradient(circle at 50% 40%,#e2b89b,var(--avatar) 60%,#6b4a36)}
.user-avatar{position:absolute;left:1092px;top:22px;width:52px;height:52px;border:3px solid var(--white)}
/* sidebar */
.sidebar{position:absolute;left:0;top:101px;width:300px;height:807px;background:var(--green);color:var(--white)}
.side-title{position:absolute;width:230px;left:59px;text-align:center;font-size:19px}
.side-rule{position:absolute;left:59px;width:241px;height:2px;background:var(--green-line)}
.group-link{position:absolute;left:61px;width:239px;height:42px;font-size:17px;line-height:22px;border-bottom:1px dashed var(--green-line)}
.group-link svg{position:absolute;right:28px;top:5px}
.btn{position:absolute;left:76px;width:176px;height:40px;border-radius:3px;font-size:16px;text-align:center;line-height:40px}
.btn-dark{background:linear-gradient(#3d3d3d,#1d1d1d);color:var(--white)}
.btn-light{background:var(--white);color:var(--text)}
/* feed */
.refine{position:absolute;left:656px;top:133px;width:205px;height:38px;border:1px solid var(--border);font-size:14px;color:#888;padding:10px 14px;background:var(--white)}
.refine-toggle{position:absolute;right:0;top:0;width:30px;height:36px;background:var(--green-soft)}
.composer{position:absolute;left:389px;top:193px;width:470px;height:45px;border:1px solid var(--border);border-top:3px solid #d8d8d8;font-size:14px;padding:12px 12px;color:#333}
.toolbar{position:absolute;left:389px;top:240px;width:470px;height:40px;border:1px solid var(--border)}
.submit{position:absolute;left:760px;top:248px;width:85px;height:27px;border-radius:4px;background:var(--green-soft);color:var(--white);font-size:14px;text-align:center;line-height:27px}
.timeline{position:absolute;left:341px;top:336px;width:2px;height:516px;background:#555}
.feed-avatar{position:absolute;width:40px;height:40px;border:2px solid #ddd}
.post{position:absolute;left:389px;width:470px;background:var(--card);border:1px solid var(--border);padding:16px 15px 0 15px}
.post-head{font-size:16px;color:#222}
.post-head span{margin-left:8px}
.post-body{margin-top:8px;font-size:12.6px;line-height:21px;letter-spacing:.15px;color:var(--muted);text-align:justify}
.reply-icon{position:absolute;right:10px;bottom:8px}
.attachment{position:absolute;left:15px;top:18px;width:52px;text-align:center;font-size:11.5px;color:var(--pdf)}
/* events */
.events{position:absolute;left:884px;top:101px;width:316px;height:807px;background:var(--panel);border-left:2px solid #dcdcdc}
.ev-title{position:absolute;left:77px;font-size:20px;color:#222}
.ev-icon{position:absolute;left:28px}
.ev-rule{position:absolute;left:27px;width:234px;height:1px;background:#d6d6d6}
.ev-item{position:absolute;left:28px;width:236px;font-size:13.4px;color:#111}
.ev-item i{position:absolute;right:0;top:1px;width:15px;height:15px;border-radius:50%;background:var(--green-soft);color:var(--white);font-style:normal;font-size:11px;font-weight:700;text-align:center;line-height:15px}
/* footer */
.footer{position:absolute;left:0;top:908px;width:1200px;height:107px;background:var(--dark);color:var(--white);font-size:13.4px}
.footer-links{position:absolute;left:61px;top:47px}
.footer-links span{margin:0 9px}
.social{position:absolute;top:33px;width:40px;height:40px;border-radius:50%;background:#3a3a3a;border:3px solid #d8d8d8}
.copyright{position:absolute;right:72px;top:47px}
</style>
</head>
<body>

<header class="topbar">
  <div class="brand">Lernwell</div>
  <nav class="topnav">
    <svg style="left:302px" width="24" height="22" viewBox="0 0 24 22"><path d="M12 1 1 11h3v10h6v-6h4v6h6V11h3z" fill="#fff"/></svg>
    <svg style="left:355px" width="22" height="22" viewBox="0 0 22 22"><rect x="1" y="3" width="20" height="18" fill="none" stroke="#fff" stroke-width="2"/><rect x="1" y="3" width="20" height="4" fill="#fff"/><rect x="5" y="0" width="2" height="5" fill="#fff"/><rect x="15" y="0" width="2" height="5" fill="#fff"/><g fill="#fff"><rect x="4" y="10" width="3" height="3"/><rect x="9.5" y="10" width="3" height="3"/><rect x="15" y="10" width="3" height="3"/><rect x="4" y="15" width="3" height="3"/><rect x="9.5" y="15" width="3" height="3"/><rect x="15" y="15" width="3" height="3"/></g></svg>
    <svg style="left:411px" width="26" height="22" viewBox="0 0 26 22"><path d="M2 11l8 8L24 3" fill="none" stroke="#fff" stroke-width="5"/></svg>
    <svg style="left:473px" width="26" height="22" viewBox="0 0 26 22"><path d="M1 3h8l2 3h11v4H6L1 20z" fill="#fff"/><path d="M6 11h19l-5 10H1z" fill="#fff"/></svg>
    <svg style="left:835px;top:40px" width="42" height="32" viewBox="0 0 42 32"><rect x="1" y="2" width="24" height="17" fill="none" stroke="#fff" stroke-width="2"/><path d="M1 2l12 10L25 2" fill="none" stroke="#fff" stroke-width="2"/><circle cx="26" cy="20" r="8" fill="#6cc04a"/></svg>
    <svg style="left:888px;top:38px" width="42" height="34" viewBox="0 0 42 34"><circle cx="12" cy="12" r="11" fill="#fff"/><path d="M7 7l10 10M17 7 7 17" stroke="#333" stroke-width="3"/><circle cx="26" cy="22" r="8" fill="#6cc04a"/></svg>
  </nav>
  <div class="user-name">MARISOL TENLEY</div>
  <div class="avatar user-avatar" role="img" aria-label="Profile photo of Marisol Tenley"></div>
</header>

<aside class="sidebar">
  <div class="side-title" style="top:26px">Teacher</div>
  <div class="side-rule" style="top:56px"></div>
  <div class="side-title" style="top:75px">My Group</div>
  <div class="group-link" style="top:130px">Group Name One<svg width="22" height="12" viewBox="0 0 22 12"><path d="M0 6h18M13 1l6 5-6 5" fill="none" stroke="#fff" stroke-width="2.4"/></svg></div>
  <div class="group-link" style="top:172px">Group Name Two<svg width="22" height="12" viewBox="0 0 22 12"><path d="M0 6h18M13 1l6 5-6 5" fill="none" stroke="#fff" stroke-width="2.4"/></svg></div>
  <div class="group-link" style="top:215px">Group Three<svg width="22" height="12" viewBox="0 0 22 12"><path d="M0 6h18M13 1l6 5-6 5" fill="none" stroke="#fff" stroke-width="2.4"/></svg></div>
  <div class="group-link" style="top:257px">Group Name 4<svg width="22" height="12" viewBox="0 0 22 12"><path d="M0 6h18M13 1l6 5-6 5" fill="none" stroke="#fff" stroke-width="2.4"/></svg></div>
  <div class="btn btn-dark" style="top:305px">Create New Group</div>
  <div class="btn btn-light" style="top:357px">Join More Groups</div>
  <div class="side-rule" style="top:410px"></div>
  <div class="side-title" style="top:432px">Community</div>
  <div class="group-link" style="top:494px;left:63px">Reading Room<svg width="22" height="12" viewBox="0 0 22 12"><path d="M0 6h18M13 1l6 5-6 5" fill="none" stroke="#fff" stroke-width="2.4"/></svg></div>
</aside>

<main>
  <div class="refine">Refine By Group<span class="refine-toggle"><svg width="30" height="36" viewBox="0 0 30 36"><path d="M9 15h12l-6 7z" fill="#fff"/></svg></span></div>
  <div class="avatar feed-avatar" style="left:323px;top:195px" role="img" aria-label="Profile photo"></div>
  <div class="composer">Please Post Your Update...</div>
  <div class="toolbar">
    <svg class="abs" style="left:284px;top:13px" width="16" height="16" viewBox="0 0 16 16"><g fill="none" stroke="#111" stroke-width="2"><rect x="1" y="6" width="7" height="5" rx="2.5" transform="rotate(-45 4.5 8.5)"/><rect x="8" y="5" width="7" height="5" rx="2.5" transform="rotate(-45 11.5 7.5)"/></g></svg>
    <svg class="abs" style="left:309px;top:12px" width="14" height="17" viewBox="0 0 14 17"><path d="M1 1h8l4 4v11H1z" fill="none" stroke="#111" stroke-width="1.6"/></svg>
    <svg class="abs" style="left:332px;top:13px" width="18" height="15" viewBox="0 0 18 15"><path d="M1 4h4l2-3h4l2 3h4v10H1z" fill="#111"/><circle cx="9" cy="8.5" r="3" fill="#fff"/></svg>
  </div>
  <div class="submit">Submit</div>

  <svg class="abs" style="left:333px;top:281px" width="24" height="24" viewBox="0 0 24 24"><path d="M19 12a7 7 0 1 1-3-5.7" fill="none" stroke="#111" stroke-width="3"/><path d="M13 2h7v7z" fill="#111"/></svg>
  <div class="timeline"></div>

  <div class="avatar feed-avatar" style="left:322px;top:330px" role="img" aria-label="Profile photo of Dorian Vask"></div>
  <article class="post" style="top:302px;height:121px">
    <div class="post-head">Dorian Vask <span>|&nbsp; 09:15 14/05/2014</span></div>
    <p class="post-body">Lorem Ipsum has been the industry's standard dummy text ever since the 1500s, when an unknown printer took a galley of type and scrambled it to the leap into electronic typesetting, remaining</p>
    <svg class="reply-icon" width="18" height="14" viewBox="0 0 18 14"><path d="M7 1 1 6l6 5V8c5 0 8 1 10 5 0-6-4-9-10-9z" fill="#8cc474"/></svg>
  </article>

  <div class="avatar feed-avatar" style="left:322px;top:470px" role="img" aria-label="Profile photo of Dorian Vask"></div>
  <article class="post" style="top:436px;height:121px">
    <div class="post-head">Dorian Vask <span>|&nbsp; 09:15 14/05/2014</span></div>
    <p class="post-body">Lorem Ipsum has been the industry's standard dummy text ever since the 1500s, when an unknown printer took a galley of type and scrambled it to the leap into electronic typesetting, remaining</p>
    <svg class="reply-icon" width="18" height="14" viewBox="0 0 18 14"><path d="M7 1 1 6l6 5V8c5 0 8 1 10 5 0-6-4-9-10-9z" fill="#8cc474"/></svg>
  </article>

  <div class="avatar feed-avatar" style="left:322px;top:602px" role="img" aria-label="Profile photo of Dorian Vask"></div>
  <article class="post" style="top:571px;height:121px;padding-left:85px">
    <div class="attachment">
      <svg width="48" height="62" viewBox="0 0 48 62"><path d="M2 2h32l12 12v46H2z" fill="#fff" stroke="#d9262c" stroke-width="2.5"/><path d="M34 2v12h12" fill="none" stroke="#d9262c" stroke-width="2.5"/><rect x="2" y="40" width="46" height="13" fill="#d9262c"/></svg>
      <div>resuts.pdf</div>
    </div>
    <div class="post-head">Dorian Vask <span>|&nbsp; 09:15 14/05/2014</span></div>
    <p class="post-body">Lorem Ipsum has been the industry's standard dummy text ever since the 1500s, when an unknown printer took a galley of type and scrambled it to the leap into electronic typesetting,</p>
    <svg class="reply-icon" width="18" height="14" viewBox="0 0 18 14"><path d="M7 1 1 6l6 5V8c5 0 8 1 10 5 0-6-4-9-10-9z" fill="#8cc474"/></svg>
  </article>

  <div class="avatar feed-avatar" style="left:381px;top:711px" role="img" aria-label="Profile photo of Elian Prowse"></div>
  <article class="post" style="top:709px;left:430px;width:429px;height:73px;padding-left:22px">
    <div class="post-head">Elian Prowse <span>|&nbsp; 09:15 14/05/2014</span></div>
    <p class="post-body" style="margin-top:4px">Thanks for this, very helpful!</p>
    <svg class="reply-icon" width="18" height="14" viewBox="0 0 18 14"><path d="M7 1 1 6l6 5V8c5 0 8 1 10 5 0-6-4-9-10-9z" fill="#8cc474"/></svg>
  </article>

  <div class="avatar feed-avatar" style="left:322px;top:828px" role="img" aria-label="Profile photo of Dorian Vask"></div>
  <article class="post" style="top:795px;height:104px">
    <div class="post-head">Dorian Vask <span>|&nbsp; 09:15 14/05/2014</span></div>
    <p class="post-body" style="text-align:left">Lorem Ipsum has been the industry's standard dummy text ever since the leap into electronic typesetting, remaining</p>
  </article>
</main>

<aside class="events">
  <svg class="ev-icon" style="top:26px" width="40" height="42" viewBox="0 0 40 42"><rect x="2" y="6" width="36" height="34" fill="#fff" stroke="#8cc474" stroke-width="3"/><rect x="2" y="6" width="36" height="8" fill="#8cc474"/><rect x="9" y="1" width="4" height="9" fill="#8cc474"/><rect x="27" y="1" width="4" height="9" fill="#8cc474"/><text x="20" y="34" font-family="Roboto,sans-serif" font-size="14" text-anchor="middle" fill="#222">10</text></svg>
  <div class="ev-title" style="top:37px">Today's Events</div>
  <div class="ev-rule" style="top:83px"></div>
  <div class="ev-item" style="top:101px">12:15am Meeting inthe canteen<i>i</i></div>
  <div class="ev-item" style="top:137px">12:54am Assignment One is due<i>i</i></div>
  <div class="ev-item" style="top:171px">12:58am New Quiz in Classroom1<i>i</i></div>
  <div class="ev-item" style="top:207px">4:15am Meeting inthe canteen<i>i</i></div>
  <div class="ev-item" style="top:243px">4:25am Meeting inthe canteen<i>i</i></div>

  <svg class="ev-icon" style="top:318px" width="40" height="42" viewBox="0 0 40 42"><rect x="2" y="6" width="36" height="34" fill="#fff" stroke="#8cc474" stroke-width="3"/><rect x="2" y="6" width="36" height="8" fill="#8cc474"/><rect x="9" y="1" width="4" height="9" fill="#8cc474"/><rect x="27" y="1" width="4" height="9" fill="#8cc474"/></svg>
  <div class="ev-title" style="top:328px">Upcoming Events</div>
  <div class="ev-rule" style="top:375px"></div>
  <div class="ev-item" style="top:392px">12:15am Meeting inthe canteen<i>i</i></div>
  <div class="ev-item" style="top:428px">4:15am Meeting inthe canteen<i>i</i></div>
  <div class="ev-item" style="top:464px">4:25am Meeting inthe canteen<i>i</i></div>
</aside>

<footer class="footer">
  <div class="footer-links">Terms<span>|</span>Privacy<span>|</span>Contact Us</div>
  <div class="social" style="left:505px"></div>
  <div class="social" style="left:560px"></div>
  <div class="social" style="left:616px"></div>
  <div class="social" style="left:671px"></div>
  <div class="copyright">Copyright © 2014 &nbsp;All Right Reserved</div>
</footer>

</body>
</html>
```